Torretta Gelato Pints

6 flavors , pints italian , southern , organic , natural feel

Pistachio , chocolate, strawberry , hazelnut , vaniglia

Stracciiatelle

Target Market(s)

Upscale

Requirements
Must have
• See graphic upload . Want that look.. showing freshbest quality in gradients of each flavor

```html
<!DOCTYPE html>
<html lang="en">
<head>
<meta charset="utf-8">
<title>Torretta Gelato – Pistachio Pint Label</title>
<link rel="stylesheet" href="https://fonts.googleapis.com/css2?family=Josefin+Sans:wght@300;400;600&family=Grand+Hotel&family=Kaushan+Script&family=Arimo:wght@400;700&display=swap">
<style>
  :root {
    --stage: #e6e6e6;
    --label: #f7f7f7;
    --ink: #1c1c1c;
    --ink-soft: #6b6b6b;
    --band: #cfcfcf;
    --band-dark: #9a9a9a;
    --gold: #c9962e;
    --pistachio: #8cbd3a;
    --pistachio-soft: #a9c94e;
    --scoop-light: #eef0d6;
    --scoop-mid: #d8e0a8;
    --flag-green: #1f9b45;
    --flag-red: #d3232f;
  }
  * { box-sizing: border-box; margin: 0; padding: 0; }
  html, body { width: 1200px; height: 857px; overflow: hidden; }
  body {
    background: var(--stage);
    font-family: "Josefin Sans", sans-serif;
    color: var(--ink);
    position: relative;
  }
  .label {
    position: absolute;
    left: 100px; top: 110px;
    width: 1000px; height: 640px;
    background: var(--label);
    box-shadow: 0 10px 30px rgba(0,0,0,.08);
  }
  .ornament-band {
    position: absolute; left: 0; top: 0;
    width: 100%; height: 90px;
    background: linear-gradient(180deg, var(--band) 0%, var(--band-dark) 50%, var(--band) 100%);
  }
  .ingredients {
    position: absolute; left: 40px; top: 130px; width: 200px;
    font-family: "Arimo", sans-serif; font-size: 12px; line-height: 1.5;
  }
  .ingredients h3 { font-size: 14px; font-weight: 700; margin-bottom: 4px; }
  .front {
    position: absolute; left: 280px; top: 110px; width: 440px; height: 510px;
    text-align: center;
  }
  .brand-name {
    font-family: "Josefin Sans", sans-serif; font-weight: 400;
    font-size: 26px; letter-spacing: 1px; color: var(--gold);
    display: flex; align-items: center; justify-content: center; gap: 10px;
    margin-top: 10px;
  }
  .brand-dot { width: 10px; height: 10px; border-radius: 50%; background: var(--gold); }
  .style-line {
    margin-top: 28px;
    font-weight: 300; font-size: 30px; letter-spacing: 1px; color: var(--ink-soft);
    display: flex; align-items: center; justify-content: center; gap: 10px;
  }
  .style-line svg { width: 26px; height: 26px; }
  .flavor-name {
    font-family: "Grand Hotel", cursive; font-size: 84px; line-height: 1;
    color: var(--pistachio); margin-top: 4px;
  }
  .organic-tag {
    position: absolute; left: 0; top: 255px;
    width: 120px; height: 44px; background: var(--pistachio-soft);
    border-radius: 4px;
    font-family: "Kaushan Script", cursive; font-size: 20px; color: #3d4f12;
    display: flex; align-items: center; justify-content: center;
  }
  .scoop-photo {
    position: absolute; left: 140px; top: 220px;
    width: 230px; height: 230px; border-radius: 50%;
    background: radial-gradient(circle at 40% 35%, var(--scoop-light) 0%, var(--scoop-mid) 70%, #b9c77a 100%);
  }
  .volume {
    position: absolute; right: 0; bottom: 0;
    width: 64px; height: 64px; border: 1px solid var(--ink); border-radius: 50%;
    font-size: 14px; display: flex; align-items: center; justify-content: center;
  }
  .nutrition {
    position: absolute; left: 760px; top: 120px; width: 210px;
    border: 1px solid var(--ink); padding: 6px 8px;
    font-family: "Arimo", sans-serif; font-size: 11px; line-height: 1.45;
  }
  .nutrition h3 { font-size: 22px; font-weight: 700; line-height: 1.1; }
  .nutrition .rule-thick { border-top: 8px solid var(--ink); margin: 3px 0; }
  .nutrition .rule-mid { border-top: 4px solid var(--ink); margin: 3px 0; }
  .nutrition .row { border-top: 1px solid var(--ink); }
  .nutrition .calories { font-size: 18px; font-weight: 700; }
  .nutrition .sub { padding-left: 12px; }
  .nutrition .sub2 { padding-left: 24px; }
  .nutrition b { font-weight: 700; }
  .nutrition .note { font-size: 9px; line-height: 1.3; margin-top: 4px; }
</style>
</head>
<body>
  <section class="label">
    <div class="ornament-band" role="img" aria-label="Decorative band of black spiral scrolls with flower medallions on white"></div>

    <div class="ingredients">
      <h3>Ingredients</h3>
      <p>Milk, Organic Cane Sugar, Cream, Pistachios, Egg Yolks.</p>
    </div>

    <div class="front">
      <div class="brand-name"><span class="brand-dot"></span>Torretta Gelato</div>
      <div class="style-line">
        ITALIAN
        <svg viewBox="0 0 26 26" aria-hidden="true">
          <clipPath id="flag-disc"><circle cx="13" cy="13" r="12"/></clipPath>
          <g clip-path="url(#flag-disc)">
            <rect x="0" y="0" width="9" height="26" fill="var(--flag-green)"/>
            <rect x="9" y="0" width="8" height="26" fill="#ffffff"/>
            <rect x="17" y="0" width="9" height="26" fill="var(--flag-red)"/>
          </g>
        </svg>
        GELATO
      </div>
      <div class="flavor-name">Pistachio</div>
      <div class="organic-tag">Organic</div>
      <div class="scoop-photo" role="img" aria-label="Photo of a scoop of pistachio gelato with pistachio sauce and a shelled nut"></div>
      <div class="volume">473ML</div>
    </div>

    <div class="nutrition">
      <h3>Nutrition Facts</h3>
      <div class="row">Serving size</div>
      <div class="rule-thick"></div>
      <div>Amount per serving</div>
      <div class="calories">Calories</div>
      <div class="rule-mid"></div>
      <div class="row"><b>Total Fat</b> 0g</div>
      <div class="row sub">Saturated Fat 0g</div>
      <div class="row sub"><i>Trans</i> Fat 0g</div>
      <div class="row"><b>Cholesterol</b> 0mg</div>
      <div class="row"><b>Sodium</b> 0mg</div>
      <div class="row"><b>Total Carbohydrate</b> 0g</div>
      <div class="row sub">Dietary Fiber 0g</div>
      <div class="row sub">Total Sugars 0g</div>
      <div class="row sub2">Includes 0g Added Sugars</div>
      <div class="row"><b>Protein</b> 0g</div>
      <div class="rule-thick"></div>
      <div>Vitamin D 0mg</div>
      <div class="row">Calcium 0mg</div>
      <div class="row">Iron 0mg</div>
      <div class="row">Potassium 0mg</div>
      <div class="rule-mid"></div>
      <p class="note">* The % Daily Value (DV) tells you how much a nutrient in a serving of food contributes to a daily diet. 2,000 calories a day is used for general nutrition advice.</p>
    </div>
  </section>
</body>
</html>
```